Printed Promo Flyer for new pet business

We need a double sided flyer design as per the given example flyer, just better looking and more fun.Flyers will need to be printed.Flyer size approx 10.5cm x 15cm. The text will need to be amended slightly afterwards to be more fun unless you can create a new tone of voice as well (should sound fun like brightly do it) Look and Feel: emotional, fun, loving, professional

Target Market(s)

Pet owners in the UK who want the convenience of getting their pets parasite treatment delivered to their door without the need of having to run to the vet or store for purchase

Industry/Entity Type

Pet Care

Colors
00a990
6b449b

Requirements
Must have
• all the content context as given in the example flyer.
Nice to have
• Tone of voice can be changed to be more fun (using Brightly as a guide)

```html
<!DOCTYPE html>
<html lang="en">
<head>
<meta charset="utf-8">
<title>Itch Parcel – Promo Flyer</title>
<link rel="stylesheet" href="https://fonts.googleapis.com/css2?family=Alfa+Slab+One&family=Roboto+Slab:wght@500&family=Arimo:wght@400;700&display=swap">
<style>
  :root{
    --purple:#6b449b;
    --teal:#00a990;
    --paper:#ececec;
    --paper-light:#f7f7f7;
    --blob:#c9c9cb;
    --ink:#1e1e1e;
    --rule:#9a9a9a;
    --page:#ffffff;
  }
  *{margin:0;padding:0;box-sizing:border-box}
  html,body{width:1200px;height:1200px;overflow:hidden;background:var(--page)}
  .flyer{
    position:absolute;left:215px;top:50px;width:770px;height:1100px;overflow:hidden;
    background:radial-gradient(ellipse at 60% 55%,var(--paper-light) 0%,var(--paper) 70%);
    font-family:"Arimo",Arial,sans-serif;color:var(--ink);
    box-shadow:0 2px 10px rgba(0,0,0,.08);
  }
  .backdrop{position:absolute;inset:0}
  .why-title{position:absolute;left:80px;top:195px;font-family:"Alfa Slab One",serif;font-weight:400;font-size:108px;line-height:1;color:var(--purple)}
  .why-sub{position:absolute;left:215px;top:305px;font-family:"Roboto Slab",serif;font-weight:500;font-size:34px;line-height:1.1;color:var(--ink)}
  .offer{position:absolute;left:620px;top:200px;width:300px;height:300px;border-radius:50%;background:var(--purple);color:#fff}
  .offer-label{position:absolute;left:22px;top:80px;width:120px;text-align:center;font-family:"Roboto Slab",serif;font-size:20px;line-height:1.1;letter-spacing:1px;padding:8px 0;border-top:2px dotted #fff;border-bottom:2px dotted #fff}
  .offer-price{position:absolute;left:18px;top:150px;width:130px;text-align:center;font-family:"Alfa Slab One",serif;font-size:36px;line-height:1}
  .features{position:absolute;left:80px;top:372px;width:460px;list-style:none}
  .feature{display:flex;align-items:center;gap:22px;height:94px;border-bottom:1.5px solid var(--rule)}
  .feature:last-child{border-bottom:none}
  .feature-icon{flex:0 0 74px;width:74px;height:74px}
  .feature-title{font-weight:700;font-size:19px;line-height:1.2;color:var(--purple);text-transform:uppercase}
  .feature-text{font-size:16px;line-height:1.2;max-width:362px}
  .photo{position:absolute;left:560px;top:505px;width:195px;height:370px;border-radius:40% 40% 30% 30%;
    background:linear-gradient(180deg,#d9b98e 0%,#c9a277 55%,#e3cfb4 100%)}
  .how-title{position:absolute;left:290px;top:762px;font-family:"Alfa Slab One",serif;font-weight:400;font-size:82px;line-height:1;color:var(--teal)}
  .how-sub{position:absolute;left:320px;top:850px;font-family:"Roboto Slab",serif;font-weight:500;font-size:30px;line-height:1.1}
  .steps{position:absolute;left:150px;top:905px;list-style:none}
  .step{display:flex;align-items:flex-start;gap:16px;font-size:19px;line-height:1.25;margin-bottom:6px}
  .step-num{flex:0 0 26px;height:26px;border-radius:50%;background:var(--purple);color:#fff;font-weight:700;font-size:15px;display:flex;align-items:center;justify-content:center}
  .paw{position:absolute;width:50px;height:50px}
</style>
</head>
<body>
<main class="flyer">
  <svg class="backdrop" width="770" height="1100" viewBox="0 0 770 1100" aria-hidden="true">
    <path d="M0 0 H770 V170 H640 C600 170 590 110 545 110 C500 110 490 175 440 175 H0 Z" fill="#ffffff"/>
    <path d="M0 740 C70 740 120 770 200 790 C300 815 320 900 260 960 C210 1010 90 1000 0 990 Z" fill="var(--blob)"/>
    <circle cx="770" cy="830" r="60" fill="var(--teal)"/>
    <circle cx="720" cy="980" r="72" fill="var(--teal)"/>
    <circle cx="790" cy="1080" r="70" fill="var(--teal)"/>
  </svg>

  <svg class="paw" style="left:590px;top:195px" viewBox="0 0 50 50" aria-hidden="true" fill="var(--teal)">
    <ellipse cx="25" cy="34" rx="12" ry="10"/><circle cx="10" cy="20" r="5"/><circle cx="19" cy="11" r="5"/><circle cx="31" cy="11" r="5"/><circle cx="40" cy="20" r="5"/>
  </svg>

  <h1 class="why-title">WHY</h1>
  <p class="why-sub">ITCH PARCEL?</p>

  <div class="offer">
    <div class="offer-label">FIRST BOX</div>
    <div class="offer-price">£5.99</div>
  </div>

  <ul class="features">
    <li class="feature">
      <svg class="feature-icon" viewBox="0 0 78 78" aria-hidden="true"><circle cx="39" cy="39" r="39" fill="var(--purple)"/><path d="M39 18 L57 25 V38 C57 50 48 57 39 61 C30 57 21 50 21 38 V25 Z" fill="none" stroke="#fff" stroke-width="3"/><path d="M30 39 L37 46 L49 32" fill="none" stroke="#fff" stroke-width="3.5" stroke-linecap="round"/></svg>
      <div><div class="feature-title">Protection &amp; Care</div><div class="feature-text">Protection against all major parasites to avoid putting your pet and your family at risk</div></div>
    </li>
    <li class="feature">
      <svg class="feature-icon" viewBox="0 0 78 78" aria-hidden="true"><circle cx="39" cy="39" r="39" fill="var(--purple)"/><circle cx="39" cy="39" r="20" fill="none" stroke="#fff" stroke-width="3"/><path d="M39 27 V39 L47 44" fill="none" stroke="#fff" stroke-width="3" stroke-linecap="round"/><path d="M17 30 L20 38 L27 33" fill="none" stroke="#fff" stroke-width="3"/></svg>
      <div><div class="feature-title">In Time</div><div class="feature-text">Never having to remember when to treat your pet</div></div>
    </li>
    <li class="feature">
      <svg class="feature-icon" viewBox="0 0 78 78" aria-hidden="true"><circle cx="39" cy="39" r="39" fill="var(--purple)"/><rect x="32" y="20" width="20" height="18" fill="#fff"/><path d="M16 48 C24 42 32 44 40 47 H56 C60 47 60 52 56 52 H34 M16 56 H50 L62 48" fill="none" stroke="#fff" stroke-width="3.5" stroke-linejoin="round"/></svg>
      <div><div class="feature-title">Convenient</div><div class="feature-text">Delivered directly to your letter box</div></div>
    </li>
    <li class="feature">
      <svg class="feature-icon" viewBox="0 0 78 78" aria-hidden="true"><circle cx="39" cy="39" r="39" fill="var(--purple)"/><path d="M29 16 H49 V36 H59 L39 60 L19 36 H29 Z" fill="none" stroke="#fff" stroke-width="3" stroke-linejoin="round"/><text x="39" y="39" text-anchor="middle" font-family="Arimo,sans-serif" font-weight="700" font-size="16" fill="#fff">£</text></svg>
      <div><div class="feature-title">Low Cost</div><div class="feature-text">All the high end, trusted brands but cheaper than the vet</div></div>
    </li>
  </ul>

  <div class="photo" role="img" aria-label="Photo of a fawn pug sitting and holding a lead in its mouth"></div>

  <h2 class="how-title">HOW</h2>
  <p class="how-sub">IT WORKS</p>

  <ol class="steps">
    <li class="step"><span class="step-num">1</span>Select which pet the treatment is for</li>
    <li class="step"><span class="step-num">2</span>Choose your treatment type</li>
    <li class="step"><span class="step-num">3</span>Select your preferred brand</li>
    <li class="step"><span class="step-num">4</span>Choose between 1, 3, 6 or 12<br>month treatment box</li>
  </ol>

  <svg class="paw" style="left:70px;top:1035px" viewBox="0 0 50 50" aria-hidden="true" fill="var(--teal)">
    <ellipse cx="25" cy="34" rx="12" ry="10"/><circle cx="10" cy="20" r="5"/><circle cx="19" cy="11" r="5"/><circle cx="31" cy="11" r="5"/><circle cx="40" cy="20" r="5"/>
  </svg>
</main>
</body>
</html>
```